Lawn Sign For Construction Projects - Vantor Power

This contest is for a lawn sign that will be placed in the front yard of recently completed construction projects. The goal here is to have a bold advertising sign that is visible from a vehicle driving past.

We are still deciding on the default size for our sign, we also may use multiple sizes. The two sizes we will more than likely be using are: 18"h x 24"w and 24"h x 36"w.

Preference will be given to designers that submit original designs that tie into our current brand and are either in both the size formats listed above or are easy to scale in photoshop or illustrator.

In the files, you will see our logo and an example of a lawn sign.

Please contact us with any questions or comments you may have!

Thank You,
- The Vantor Power Team

Industry/Entity Type

Residential Construction

Colors
34a7d8
ffffff
faa54b

Requirements
Nice to have
• 1. The sign must tie into our current branding and color scheme.
• 2. The sign must be clearly visible and readable.
• 3. The sign must include our phone number in readable print.
• 4. Our website written in small print along the bottom of the sign.
• 5. Must mention we install the following products:
• a.) Solar
• b.) Roofing
• c.) Windows
• d.) Artificial Lawn
• e.) Whole House Fans
• f.) Patio Covers

```html
<!DOCTYPE html>
<html lang="en">
<head>
<meta charset="utf-8">
<title>Vantor Power – Lawn Sign</title>
<link rel="stylesheet" href="https://fonts.googleapis.com/css2?family=Montserrat:wght@700;800;900&display=swap">
<style>
  :root {
    --sign-black: #050505;
    --frame: #1c1c1c;
    --brand-blue: #34a7d8;
    --brand-orange: #faa54b;
    --accent-orange: #ef7d22;
    --accent-blue: #2d7fd0;
    --white: #ffffff;
  }
  html, body {
    margin: 0;
    width: 1200px;
    height: 800px;
    overflow: hidden;
    background: #e9ecef;
  }
  .lawn-sign {
    position: relative;
    box-sizing: border-box;
    width: 1200px;
    height: 800px;
    background: var(--sign-black);
    border: 14px solid var(--frame);
    font-family: "Montserrat", Arial, sans-serif;
    color: var(--white);
  }
  .stripe {
    position: absolute;
    top: 70px;
    bottom: 70px;
    width: 14px;
  }
  .stripe--left-blue { left: 70px; background: var(--brand-blue); }
  .stripe--left-orange { left: 100px; background: var(--brand-orange); }
  .stripe--right-orange { right: 110px; background: var(--accent-orange); }
  .stripe--right-blue { right: 78px; background: var(--accent-blue); }

  .sign-content {
    position: absolute;
    left: 160px;
    right: 160px;
    top: 0;
    bottom: 0;
    display: flex;
    flex-direction: column;
    align-items: center;
    text-align: center;
  }
  .sign-content p, .sign-content h1 { margin: 0; }
  .brand-dot {
    margin-top: 66px;
    width: 100px;
    height: 100px;
    border-radius: 50%;
    background: var(--accent-orange);
  }
  .brand-name {
    margin-top: 22px !important;
    font-size: 92px;
    font-weight: 800;
    letter-spacing: 2px;
    line-height: 1;
    color: var(--accent-blue);
    text-transform: uppercase;
    white-space: nowrap;
  }
  .tagline {
    margin-top: 14px !important;
    font-size: 42px;
    font-weight: 800;
    line-height: 1.2;
    letter-spacing: 2px;
    color: var(--accent-orange);
    text-transform: uppercase;
  }
  .products {
    margin-top: 16px !important;
    font-size: 24px;
    font-weight: 700;
    line-height: 1.35;
    letter-spacing: 1px;
    text-transform: uppercase;
  }
  .products .sep { color: var(--brand-blue); padding: 0 6px; }
  .phone {
    margin-top: 30px !important;
    font-size: 104px;
    font-weight: 900;
    line-height: 1;
    letter-spacing: 1px;
  }
  .website {
    margin-top: 20px !important;
    font-size: 38px;
    font-weight: 800;
    line-height: 1.2;
    letter-spacing: 1px;
  }
</style>
</head>
<body>
  <main class="lawn-sign">
    <div class="stripe stripe--left-blue"></div>
    <div class="stripe stripe--left-orange"></div>
    <div class="stripe stripe--right-orange"></div>
    <div class="stripe stripe--right-blue"></div>

    <section class="sign-content">
      <div class="brand-dot"></div>
      <h1 class="brand-name">Vantor Power</h1>
      <p class="tagline">We’ve Gone Solar!</p>
      <p class="products">
        Solar<span class="sep">•</span>Roofing<span class="sep">•</span>Windows<br>
        Artificial Lawn<span class="sep">•</span>Whole House Fans<span class="sep">•</span>Patio Covers
      </p>
      <p class="phone">123.456.7890</p>
      <p class="website">WWW.VANTORPOWER.COM</p>
    </section>
  </main>
</body>
</html>
```